Design Letterhead, Business Card and ID Card

I need minimalistic design for Letterhead, Business Card and ID Card. Simple and elegant design. Dumny text for address, phone number etc. Logo file attached

```html
<!DOCTYPE html>
<html lang="en">
<head>
<meta charset="utf-8">
<title>Plum Crush — Business Card</title>
<link rel="stylesheet" href="https://fonts.googleapis.com/css2?family=Montserrat:wght@400;500;600;700&display=swap">
<style>
  :root {
    --backdrop: #1d1d1f;
    --card-white: #ffffff;
    --plum: #5b2370;
    --plum-mark: #7a2f91;
    --leaf: #2f9e48;
    --leaf-soft: #4caf5f;
    --ink: #262626;
    --on-plum: #ffffff;
  }
  * { margin: 0; padding: 0; box-sizing: border-box; }
  html, body {
    width: 1200px; height: 900px; overflow: hidden;
    background: var(--backdrop);
    font-family: "Montserrat", sans-serif;
  }
  .stage { position: relative; width: 1200px; height: 900px; }
  .card {
    position: absolute; left: 290px; width: 620px; height: 354px;
    background: var(--card-white); overflow: hidden;
  }
  .card--front { top: 80px; }
  .card--back { top: 466px; }

  .brand { display: flex; align-items: center; gap: 14px; }
  .brand__dot { width: 30px; height: 30px; border-radius: 50%; background: var(--plum-mark); flex: none; }
  .brand__name { font-weight: 500; color: var(--ink); letter-spacing: 0.5px; }

  .card--front .brand {
    position: absolute; left: 50%; top: 50%; transform: translate(-50%, -50%);
  }
  .card--front .brand__name { font-size: 40px; }

  .back-art { position: absolute; inset: 0; }
  .card--back .brand { position: absolute; right: 52px; top: 92px; }
  .card--back .brand__dot { width: 24px; height: 24px; }
  .card--back .brand__name { font-size: 30px; }

  .leaf-illustration {
    position: absolute; left: 206px; top: 30px; width: 48px; height: 52px;
    background: linear-gradient(160deg, var(--leaf-soft), var(--leaf));
    border-radius: 6px;
  }

  .contact { position: absolute; left: 40px; top: 96px; color: var(--on-plum); }
  .contact__name { font-size: 19px; font-weight: 600; text-transform: uppercase; letter-spacing: 0.3px; }
  .contact__name span { color: var(--leaf); }
  .contact__role { font-size: 12px; font-weight: 600; margin-top: 2px; }
  .contact__address { font-size: 12.5px; line-height: 1.5; margin-top: 22px; }
  .contact__lines { list-style: none; margin-top: 22px; font-size: 12.5px; }
  .contact__lines li { display: flex; align-items: center; gap: 10px; line-height: 1.55; }
  .contact__lines svg { width: 12px; height: 12px; flex: none; }
</style>
</head>
<body>
<main class="stage">

  <section class="card card--front">
    <div class="brand">
      <span class="brand__dot"></span>
      <span class="brand__name">plum crush</span>
    </div>
  </section>

  <section class="card card--back">
    <svg class="back-art" viewBox="0 0 620 354" aria-hidden="true">
      <rect width="620" height="354" fill="var(--plum)"/>
      <circle cx="560" cy="70" r="300" fill="var(--card-white)"/>
    </svg>
    <div class="leaf-illustration" role="img" aria-label="Leaf and stem illustration"></div>

    <div class="brand">
      <span class="brand__dot"></span>
      <span class="brand__name">plum crush</span>
    </div>

    <div class="contact">
      <p class="contact__name"><span>Dana</span> Whitfield</p>
      <p class="contact__role">General Manager</p>
      <p class="contact__address">418 Orchard Lane,<br>Suite 204 Fairview, OR 9731</p>
      <ul class="contact__lines">
        <li>
          <svg viewBox="0 0 12 12"><path d="M2 1h3l1 3-1.5 1a6 6 0 0 0 2.5 2.5L8 6l3 1v3a1 1 0 0 1-1 1A9 9 0 0 1 1 2a1 1 0 0 1 1-1z" fill="var(--on-plum)"/></svg>
          +1 555 010 2040
        </li>
        <li>
          <svg viewBox="0 0 12 12"><rect x="3" y="0.5" width="6" height="11" rx="1" fill="none" stroke="var(--on-plum)" stroke-width="1.2"/></svg>
          +1 555 010 3311
        </li>
        <li>
          <svg viewBox="0 0 12 12"><rect x="0.5" y="2" width="11" height="8" fill="var(--on-plum)"/><path d="M0.5 2 6 7l5.5-5" fill="none" stroke="var(--plum)" stroke-width="1"/></svg>
          info@plumcrush.example
        </li>
        <li>
          <svg viewBox="0 0 12 12"><circle cx="6" cy="6" r="5.4" fill="none" stroke="var(--on-plum)" stroke-width="1.1"/><path d="M0.6 6h10.8M6 0.6c2.5 3 2.5 7.8 0 10.8M6 0.6c-2.5 3-2.5 7.8 0 10.8" fill="none" stroke="var(--on-plum)" stroke-width="0.9"/></svg>
          www.plumcrush.example
        </li>
      </ul>
    </div>
  </section>

</main>
</body>
</html>
```